WeatheredIt.net wordpress design

Concept: Website where personal stories, personal videos can be posted as a challenge while awaiting the wisdom of experience from others who have survived this same event or challenge in their lifetime.
Support aspects will be in 4 quadrants of Challenges:
1. Financial 2. Medical & Physical
3. Legal Matters 4. Psychological & Spiritual - ability to chat online with a spiritual/psychological counselor or life coach
Updates
Project Deadline Extended
Reason: Bit more time to complete designs.
Wanted to thank all of you for your designs! Greatly appreciated. Very creative ideas that captured the essence of this website. Will be back with a selection very shortly.
Target Market(s)
Anyone looking for a solution based upon experiential wisdom
Industry/Entity Type
Financial
Requirements
Must have
- Interactive website: Where you can post a challenge or issue via a written question or a video and ask for a solution.
Ability to access any of the 4 Quadrants (as listed above) to ask for an expert, via experience, advice and wisdom from those who have similar challenges.

```html
<!DOCTYPE html>
<html lang="en">
<head>
<meta charset="utf-8">
<title>WeatheredIt.net</title>
<link href="https://fonts.googleapis.com/css2?family=Questrial&family=Mulish:wght@400;600;700&display=swap" rel="stylesheet">
<style>
:root{
  --red:#d9424f;
  --red-dark:#c22a39;
  --red-light:#e8647a;
  --orange:#f5a20f;
  --orange-text:#d98a06;
  --ink:#222;
  --text:#555;
  --muted:#777;
  --line:#ccc;
  --panel:#fff;
  --page:#e6e6e6;
  --btn:#1b1b1b;
  --pill:#8f8f8f;
}
*{box-sizing:border-box;margin:0;padding:0}
html,body{width:1063px;height:1200px;overflow:hidden}
body{position:relative;background:var(--page);font-family:"Questrial",sans-serif;color:var(--text)}
.hero{position:absolute;left:0;top:0;width:1063px;height:442px;
  background:radial-gradient(ellipse at 50% 35%,var(--red-light) 0%,var(--red) 55%,var(--red-dark) 100%);
  border-top:3px solid var(--orange)}
.topnav{position:absolute;left:126px;top:3px;width:841px;height:27px;background:var(--panel);
  display:flex;align-items:center;font-size:14px}
.topnav a{color:#444;text-decoration:none;padding:0 22px;border-right:1px solid var(--line);line-height:18px}
.topnav a:first-child{font-weight:700;font-family:"Mulish",sans-serif;color:var(--ink);padding-left:18px}
.topnav a:nth-child(4){border:none}
.account{margin-left:auto;display:flex;align-items:center;font-family:"Mulish",sans-serif;font-size:10px;font-weight:700}
.account span{color:var(--ink);text-decoration:underline;margin:0 10px}
.search{display:flex;margin:0 5px 0 6px;border:1px solid #999;height:18px}
.search input{width:129px;border:none;font:italic 11px "Questrial",sans-serif;padding-left:5px;color:#999}
.search button{width:23px;background:var(--btn);color:#fff;border:none;font:700 11px "Mulish",sans-serif}
.brand{position:absolute;left:126px;top:58px;width:161px;height:73px;background:var(--panel);border-radius:3px;
  display:flex;align-items:center;gap:8px;padding-left:10px}
.brand i{width:26px;height:26px;background:var(--orange);display:block}
.brand b{font-family:"Mulish",sans-serif;font-weight:700;font-size:15px;color:var(--orange-text)}
.hero-photo{position:absolute;left:290px;top:30px;width:440px;height:412px;
  background:radial-gradient(closest-side at 48% 50%,#d9b39a 0%,#8a6a5a 40%,#3a3e48 80%,rgba(58,62,72,0) 100%)}
.hero-caption{position:absolute;left:490px;top:358px;color:#fff}
.hero-caption h2{font-weight:400;font-size:21px}
.hero-caption h2 b{font-family:"Mulish",sans-serif;font-weight:700}
.hero-caption p{font-size:11.5px}
.dots{position:absolute;left:127px;top:389px;display:flex;gap:4px}
.dots i{width:9px;height:9px;border-radius:50%;background:#eee;display:block}
.dots i:first-child{background:var(--orange);border:2px solid #fff}
.ask{position:absolute;left:725px;top:58px;width:242px;height:338px;background:var(--panel);border-radius:3px;padding:26px 11px 0 11px}
.ask h3{font-weight:400;font-size:20px;color:#444}
.ask p{font-size:12px;line-height:14px;margin:6px 0 16px}
.field{border:1px solid var(--line);border-radius:3px;height:24px;font-size:12px;color:#aaa;padding:4px 6px;margin-bottom:4px}
.field.tall{height:92px}
.row{display:flex;gap:4px}
.row .field{flex:1}
.row .field.btn{flex:0 0 64px;text-align:center}
.btn-dark{display:block;background:var(--btn);color:#fff;font:700 12px "Mulish",sans-serif;text-align:center;border-radius:3px;height:23px;line-height:23px}
.content{position:absolute;left:126px;top:424px;width:841px;height:642px;background:var(--panel)}
.section-title{position:absolute;font-size:19px;color:#444;font-weight:400}
.rule{position:absolute;height:1px;background:linear-gradient(90deg,rgba(0,0,0,0),#ccc 50%,rgba(0,0,0,0))}
.article{position:absolute;left:16px;width:366px}
.article h4{font-family:"Mulish",sans-serif;font-weight:600;font-size:13.5px;color:var(--ink)}
.meta{font-family:"Mulish",sans-serif;font-weight:600;font-size:9.5px;line-height:11.5px;color:var(--orange-text)}
.shares{display:flex;gap:2px;margin:3px 0 4px}
.shares i{width:14px;height:14px;display:block;border-radius:2px;background:var(--orange)}
.shares i:nth-child(3){background:#3b5c9c}.shares i:nth-child(4){background:#c9c9c9}
.shares i:nth-child(5){background:#46b3e6}.shares i:nth-child(6){background:#e0508a}
.article p{font-size:11px;line-height:13px;color:#666}
.pill{display:inline-block;background:var(--pill);color:#fff;font-size:11px;border-radius:4px;padding:0 8px;line-height:14px;margin-top:2px;border:1px solid #777}
.quad{position:absolute;width:170px}
.quad h5{font-family:"Mulish",sans-serif;font-weight:700;font-size:15.5px;color:var(--ink);line-height:18px;margin-bottom:9px}
.entry{font-size:10.5px;line-height:13px;color:var(--muted);margin-bottom:6px}
.entry b{font-family:"Mulish",sans-serif;font-weight:600;color:#444}
.chat{position:absolute;left:482px;top:511px;width:222px}
.chat h3{font-weight:400;font-size:19px;line-height:22px;color:#444}
.chat p{font-size:12px;line-height:14px;margin:10px 0 8px}
</style>
</head>
<body>
<header class="hero">
  <nav class="topnav">
    <a>Home</a><a>Profile</a><a>Followers</a><a>My Uploads</a>
    <div class="account"><span>Login</span>|<span>Register</span>
      <div class="search"><input value="search"><button>Go</button></div></div>
  </nav>
  <div class="brand"><i></i><b>WeatheredIt.net</b></div>
  <div class="hero-photo" role="img" aria-label="Portrait photo of a smiling older man in a suit"></div>
  <div class="hero-caption"><h2>Learn from <b>Experience</b></h2><p>Experience is the best teacher overall</p></div>
  <div class="dots"><i></i><i></i><i></i><i></i><i></i></div>
  <form class="ask">
    <h3>Ask your Question</h3>
    <p>and get answered by the experienced people around the world</p>
    <div class="field">Name</div>
    <div class="field">email address</div>
    <div class="field tall">your question</div>
    <div class="field">Select Quadrant</div>
    <div class="row"><div class="field">Upload Video (optional)</div><div class="field btn">Browse</div></div>
    <span class="btn-dark">Get Answer</span>
  </form>
</header>

<main class="content">
  <h2 class="section-title" style="left:14px;top:12px">Fresh Articles</h2>
  <h2 class="section-title" style="left:484px;top:12px">Browse by Quadrant</h2>
  <div class="rule" style="left:140px;top:42px;width:670px"></div>

  <article class="article" style="top:65px"><h4>Problem in life with Money</h4><div class="meta">July 13, 2012<br>132 response, 8996 views</div><div class="shares"><i></i><i></i><i></i><i></i><i></i><i></i></div><p>This is Draftly's version  of Lorem Ipsum. Proin gravida nibh vel velit auctor aliquet. Aenean sollicitudin, lorem quis bibendum auctor, nisi elit consequat ipsum, nec sagittis sem nibh id elit. Duis sed ...</p><span class="pill">more</span></article>
  <article class="article" style="top:208px"><h4>Problem in life with Money</h4><div class="meta">July 13, 2012<br>132 response, 8996 views</div><div class="shares"><i></i><i></i><i></i><i></i><i></i><i></i></div><p>This is Draftly's version  of Lorem Ipsum. Proin gravida nibh vel velit auctor aliquet. Aenean sollicitudin, lorem quis bibendum auctor, nisi elit consequat ipsum, nec sagittis sem nibh id elit. Duis sed ...</p><span class="pill">more</span></article>
  <article class="article" style="top:351px"><h4>Problem in life with Money</h4><div class="meta">July 13, 2012<br>132 response, 8996 views</div><div class="shares"><i></i><i></i><i></i><i></i><i></i><i></i></div><p>This is Draftly's version  of Lorem Ipsum. Proin gravida nibh vel velit auctor aliquet. Aenean sollicitudin, lorem quis bibendum auctor, nisi elit consequat ipsum, nec sagittis sem nibh id elit. Duis sed ...</p><span class="pill">more</span></article>
  <article class="article" style="top:494px"><h4>Problem in life with Money</h4><div class="meta">July 13, 2012<br>132 response, 8996 views</div><div class="shares"><i></i><i></i><i></i><i></i><i></i><i></i></div><p>This is Draftly's version  of Lorem Ipsum. Proin gravida nibh vel velit auctor aliquet. Aenean sollicitudin, lorem quis bibendum auctor, nisi elit consequat ipsum, nec sagittis sem nibh id elit. Duis sed ...</p><span class="pill">more</span></article>

  <section class="quad" style="left:483px;top:70px"><h5>Financial Problems</h5>
    <div class="entry"><b>Problem in life with Money</b><br>July 13, 2012<br>132 response, 8996 views</div>
    <div class="entry"><b>Problem in life with Money</b><br>July 13, 2012<br>132 response, 8996 views</div>
    <div class="entry"><b>Problem in life with Money</b><br>July 13, 2012<br>132 response, 8996 views</div><span class="pill">more</span></section>
  <section class="quad" style="left:671px;top:70px"><h5>Legal Matters</h5>
    <div class="entry"><b>Problem in life with Money</b><br>July 13, 2012<br>132 response, 8996 views</div>
    <div class="entry"><b>Problem in life with Money</b><br>July 13, 2012<br>132 response, 8996 views</div>
    <div class="entry"><b>Problem in life with Money</b><br>July 13, 2012<br>132 response, 8996 views</div><span class="pill">more</span></section>
  <section class="quad" style="left:483px;top:290px"><h5>Medical &amp; Physical</h5>
    <div class="entry"><b>Problem in life with Money</b><br>July 13, 2012<br>132 response, 8996 views</div>
    <div class="entry"><b>Problem in life with Money</b><br>July 13, 2012<br>132 response, 8996 views</div>
    <div class="entry"><b>Problem in life with Money</b><br>July 13, 2012<br>132 response, 8996 views</div><span class="pill">more</span></section>
  <section class="quad" style="left:671px;top:290px"><h5>Psychological &amp;<br>Spiritual</h5>
    <div class="entry"><b>Problem in life with Money</b><br>July 13, 2012<br>132 response, 8996 views</div>
    <div class="entry"><b>Problem in life with Money</b><br>July 13, 2012<br>132 response, 8996 views</div><span class="pill">more</span></section>

  <div class="rule" style="left:500px;top:496px;width:310px"></div>
  <section class="chat"><h3>Chat Online with a<br>Life Coach</h3><p>and get answered by the experienced people around the world</p><span class="btn-dark">Start Now</span></section>
</main>
</body>
</html>
```